Pop-up Banner

Would like a design for a pop-up 85 x 206cm banner for a trade show. (from norla press)
We would like "our logo" (brightwave holdings) - then the tagline - "Your Trusted Partner in Data-Driven Decisions"
*Supporting Bullets*
Unified data, analytics & AI
Trusted insights, faster outcomes
Real-time intelligence at scale
Enterprise-ready, secure solutions
Clarity from data complexity
trusted by...some company logos
Partners with : partner logo
Our Colours: #FFA300, #3D4176, #FDD16E, #F87C57, #A68118, #1C2F36

```html
<!DOCTYPE html>
<html lang="en">
<head>
<meta charset="utf-8">
<title>Brightwave Holdings – Pop-up Banner</title>
<link rel="stylesheet" href="https://fonts.googleapis.com/css2?family=Poppins:wght@500;600;700;800&display=swap">
<style>
:root{
  --orange:#FFA300;
  --indigo:#3D4176;
  --butter:#FDD16E;
  --coral:#F87C57;
  --ochre:#A68118;
  --ink:#1C2F36;
  --stage:#9e9e9e;
  --tile:#EFEFEF;
  --white:#ffffff;
}
*{box-sizing:border-box;margin:0;padding:0}
html,body{width:1200px;height:2434px;overflow:hidden}
body{background:var(--stage);font-family:"Poppins",sans-serif;position:relative}
.banner{position:absolute;left:148px;top:148px;width:883px;height:2141px;background:var(--white);box-shadow:0 6px 24px rgba(0,0,0,.35);overflow:hidden}
.header{position:absolute;left:0;top:0;width:100%;height:230px;background:var(--indigo)}
.header-pointer{position:absolute;left:421px;top:229px;width:0;height:0;border-left:21px solid transparent;border-right:21px solid transparent;border-top:30px solid var(--indigo)}
.brand{position:absolute;left:0;top:0;width:100%;height:230px;display:flex;align-items:center;justify-content:center;gap:26px}
.brand-dot{width:110px;height:110px;border-radius:50%;border:20px solid var(--orange)}
.brand-name{color:var(--orange);font-weight:700;font-size:47px;line-height:50px;letter-spacing:1px}
.headline{position:absolute;left:0;top:268px;width:100%;text-align:center;font-weight:800;font-size:80px;line-height:75px;letter-spacing:-1px;color:var(--ink);text-transform:uppercase}
.headline .accent{color:var(--indigo)}
.services-zone{position:absolute;left:0;top:676px;width:100%;height:926px;background:linear-gradient(180deg,#FDBB35 0%,var(--orange) 100%)}
.photo{position:absolute;left:117px;top:616px;width:653px;height:370px;background:var(--white);padding:7px;box-shadow:0 18px 24px rgba(0,0,0,.35)}
.photo-fill{width:100%;height:100%;background:linear-gradient(110deg,#3a3a48 0%,#6f6a72 35%,#6f82c8 65%,#9fb4ea 100%)}
.section-title{position:absolute;left:0;width:100%;text-align:center;font-weight:800;color:var(--indigo);letter-spacing:5px;text-transform:uppercase}
.services-title{top:1040px;font-size:52px}
.service{position:absolute;left:114px;width:656px;height:83px;background:var(--ink);border-radius:18px;display:flex;align-items:center;box-shadow:0 2px 0 rgba(0,0,0,.25)}
.service svg{width:72px;height:64px;margin-left:14px;flex:none}
.service span{margin-left:12px;color:var(--white);font-weight:600;font-size:31px;white-space:nowrap}
.zone-pointer{position:absolute;left:426px;top:1580px;width:0;height:0;border-left:16px solid transparent;border-right:16px solid transparent;border-bottom:22px solid var(--white)}
.partners-title{top:1638px;font-size:38px}
.partners{position:absolute;left:112px;top:1716px;width:660px;display:grid;grid-template-columns:repeat(3,215px);grid-auto-rows:84px;gap:6px 7px}
.partner{background:var(--tile);display:flex;align-items:center;justify-content:center;gap:10px;color:var(--indigo);font-weight:600;font-size:28px}
.partner i{display:block;width:22px;height:22px;background:var(--indigo)}
.url{position:absolute;left:0;top:2000px;width:100%;text-align:center;font-weight:700;font-size:42px;color:#2a2a2a}
.footer-bar{position:absolute;left:0;bottom:0;width:100%;height:16px;background:var(--indigo)}
</style>
</head>
<body>
<main class="banner">
  <header class="header">
    <div class="brand">
      <div class="brand-dot"></div>
      <div class="brand-name">BRIGHTWAVE<br>HOLDINGS</div>
    </div>
  </header>
  <div class="header-pointer"></div>

  <h1 class="headline">Your Trusted<br>Partner in<br><span class="accent">Data-Driven<br>Decisions</span></h1>

  <section class="services-zone"></section>
  <div class="photo"><div class="photo-fill" role="img" aria-label="Photo of a professional pointing at large data dashboards on a wall screen"></div></div>

  <h2 class="section-title services-title">Our Services</h2>

  <div class="service" style="top:1133px">
    <svg viewBox="0 0 72 64"><path d="M18 50a12 12 0 0 1 0-24 18 18 0 0 1 34-4 13 13 0 0 1 4 28z" fill="var(--butter)"/><rect x="28" y="34" width="18" height="16" rx="2" fill="var(--ink)"/><path d="M31 34v-5a6 6 0 0 1 12 0v5" fill="none" stroke="var(--ink)" stroke-width="3"/></svg>
    <span>Unified data, analytics &amp; AI</span>
  </div>
  <div class="service" style="top:1221px">
    <svg viewBox="0 0 72 64"><rect x="12" y="10" width="48" height="34" rx="3" fill="var(--butter)"/><rect x="6" y="46" width="60" height="6" rx="2" fill="var(--butter)"/><path d="M36 14l10 4v8c0 6-5 10-10 12-5-2-10-6-10-12v-8z" fill="var(--ink)"/></svg>
    <span>Trusted insights, faster outcomes</span>
  </div>
  <div class="service" style="top:1308px">
    <svg viewBox="0 0 72 64"><path d="M34 6c-12 0-20 8-20 18-6 4-6 16 2 20 0 8 8 14 18 12z" fill="var(--butter)"/><g stroke="var(--butter)" stroke-width="3" fill="none"><path d="M38 16h12M38 28h20M38 40h14M38 52h10"/></g><g fill="var(--butter)"><circle cx="52" cy="16" r="3"/><circle cx="60" cy="28" r="3"/><circle cx="54" cy="40" r="3"/><circle cx="50" cy="52" r="3"/></g></svg>
    <span>Real-time intelligence at scale</span>
  </div>
  <div class="service" style="top:1396px">
    <svg viewBox="0 0 72 64"><g fill="var(--butter)"><rect x="10" y="38" width="9" height="20"/><rect x="24" y="30" width="9" height="28"/><rect x="38" y="36" width="9" height="22"/><rect x="52" y="22" width="9" height="36"/><rect x="4" y="58" width="64" height="3"/></g><path d="M14 26l14-10 14 8 16-16" stroke="var(--butter)" stroke-width="3" fill="none"/></svg>
    <span>Enterprise-ready, secure solutions</span>
  </div>
  <div class="service" style="top:1485px">
    <svg viewBox="0 0 72 64"><path d="M16 34a12 12 0 0 1 4-23 16 16 0 0 1 30 2 11 11 0 0 1 6 21z" fill="var(--butter)"/><ellipse cx="36" cy="36" rx="14" ry="5" fill="var(--ink)"/><path d="M22 36v18c0 3 6 6 14 6s14-3 14-6V36c0 3-6 6-14 6s-14-3-14-6z" fill="var(--butter)"/><path d="M22 45c0 3 6 6 14 6s14-3 14-6" stroke="var(--ink)" stroke-width="2" fill="none"/></svg>
    <span>Clarity from data complexity</span>
  </div>
  <div class="zone-pointer"></div>

  <h2 class="section-title partners-title">Our Partners</h2>
  <div class="partners">
    <div class="partner"><i></i>Harbourline</div>
    <div class="partner">Quantis</div>
    <div class="partner">Veltra</div>
    <div class="partner">Corvan</div>
    <div class="partner"><i></i>Maplecore</div>
    <div class="partner">Flintkit</div>
    <div class="partner">clearlogic</div>
    <div class="partner">Orenda</div>
    <div class="partner"><i style="border-radius:50%"></i>Ravelle</div>
  </div>

  <p class="url">www.brightwave-holdings.com</p>
  <div class="footer-bar"></div>
</main>
</body>
</html>
```